Photo-Video Combo Package Flyer

Need to create a flyer to showcase a combo package featuring photography and videography from two separate companies. I need an 8 1/2 X 11 flyer in .psd so I can make changes as needed as well as all fonts
Target Market(s)
Brides & Grooms
Industry/Entity Type
Wedding Photography
Requirements
Must have
- see word doc
Nice to have
- please visit websites for inspiration
- https://brightoakportraitstudio.com/
- www.qmtrz.com

```html
<!DOCTYPE html>
<html lang="en">
<head>
<meta charset="utf-8">
<title>Photo-Video Combo Package Flyer</title>
<link href="https://fonts.googleapis.com/css2?family=Open+Sans:wght@400;600&family=Roboto+Slab:wght@500;700&display=swap" rel="stylesheet">
<style>
:root{
  --page:#eeeeee;
  --paper:#ffffff;
  --salmon:#c9826f;
  --periwinkle:#8794c4;
  --grey-light:#e6e6e6;
  --grey-mid:#c9c9c9;
  --frame:#9a9a9a;
  --ink:#333333;
  --ink-soft:#4a4a4a;
  --badge:#d8141c;
}
*{box-sizing:border-box;margin:0;padding:0}
html,body{width:768px;height:1200px;overflow:hidden;background:var(--page)}
body{position:relative;font-family:"Open Sans",Arial,sans-serif;color:var(--ink)}
.flyer{position:absolute;left:34px;top:150px;width:700px;height:897px;background:var(--paper);box-shadow:0 10px 30px rgba(0,0,0,.15);overflow:hidden}
.abs{position:absolute}
.brand{left:0;width:335px;text-align:center;font-family:"Open Sans",Arial,sans-serif;font-weight:600}
.brand-photo{top:24px;color:var(--salmon);font-size:22px;letter-spacing:.5px}
.brand-video{top:78px;color:var(--periwinkle);font-size:26px;display:flex;justify-content:center;align-items:center;gap:10px}
.brand-video .dot{width:18px;height:18px;border-radius:50%;background:var(--periwinkle)}
.intro{left:49px;top:152px;width:260px;font-size:10.6px;line-height:13.6px;text-align:justify}
.accent-stripe{left:335px;top:0;width:8px;height:438px;background:var(--salmon)}
.hero{left:343px;top:0;width:357px;height:438px;background:linear-gradient(120deg,#d9d4cc 0%,#ece9e4 40%,#c8cfc7 75%,#e8e2da 100%)}
.note{left:36px;top:277px;width:282px;height:56px;background:var(--grey-light);padding:9px 20px;font-size:11.4px;line-height:15px;color:var(--ink-soft)}
.offer{left:36px;top:341px;width:282px;height:96px;background:var(--grey-mid);padding:8px 20px;font-family:"Roboto Slab",Georgia,serif;font-weight:700;font-size:13.4px;line-height:17px;color:var(--ink)}
.offer p+p{margin-top:12px}
.gallery{left:0;top:445px;width:700px;height:162px;background:var(--grey-mid)}
.gallery-gap{left:363px;top:445px;width:9px;height:162px;background:var(--paper)}
.shot{top:445px;height:162px}
.shot-deck{left:45px;width:318px;background:linear-gradient(180deg,#6d6f8c 0%,#d69a72 45%,#7a6a72 65%,#4a4c5e 100%)}
.shot-pier{left:372px;width:290px;background:linear-gradient(180deg,#3d4e78 0%,#6c7aa0 45%,#35506a 70%,#1f3a4c 100%)}
.package{top:645px;width:294px;height:178px;border:2px solid var(--frame);border-top:none}
.package::before{content:"";position:absolute;top:0;right:-2px;width:108px;border-top:2px solid var(--frame)}
.package-photo{left:43px}
.package-video{left:383px}
.package h2{position:absolute;top:-10px;left:18px;font-family:"Roboto Slab",Georgia,serif;font-weight:700;font-size:13.5px;color:var(--ink);background:var(--paper);padding-right:6px;white-space:nowrap}
.package .icon{position:absolute;top:-17px;left:-14px;width:26px;height:24px}
.package ul{list-style:none;position:absolute;top:23px;left:14px;right:8px;font-size:10px;line-height:13px;color:var(--ink-soft)}
.package li{position:relative;padding-left:13px;margin-bottom:6.5px}
.package li svg{position:absolute;left:0;top:2px;width:9px;height:9px}
.badge{left:305px;top:685px;width:92px;height:92px}
.band{left:0;width:700px;height:22px;color:#fff;font-family:"Roboto Slab",Georgia,serif;font-size:13px;display:flex;align-items:center;justify-content:center;gap:10px;white-space:nowrap}
.band .label{font-family:"Open Sans",Arial,sans-serif}
.band b{font-weight:700}
.band .sep{opacity:.9}
.band-photo{top:846px;background:var(--salmon)}
.band-video{top:873px;background:var(--periwinkle)}
</style>
</head>
<body>
<main class="flyer">
  <div class="abs brand brand-photo">Bright Oak Portrait Studio</div>
  <div class="abs brand brand-video"><span class="dot"></span>Quill Motion Reels</div>

  <p class="abs intro">The Photo-Video combo package is the best way to hire your Photographer and videographer. Both companies are highly rated by The Vow Guide and Aisle Ledger as well as recommended by the area's top wedding venues. When your photographer and videographer are working together your wedding day will run smoothly, so you can just enjoy yourself and have fun!</p>

  <div class="abs accent-stripe"></div>
  <div class="abs hero" role="img" aria-label="Portrait of a bride in a lace halter gown holding a white bouquet"></div>

  <div class="abs note">Contact us to learn more and schedule a consultation. Photography provided by Bright Oak Portrait Studio</div>
  <div class="abs offer">
    <p>Videography provided by Quill Motion Reels</p>
    <p>Photo Video Combo Price<br>$2999 ($750 Savings)</p>
  </div>

  <div class="abs gallery"></div>
  <div class="abs gallery-gap"></div>
  <div class="abs shot shot-deck" role="img" aria-label="Couple embracing on a ship deck at sunset"></div>
  <div class="abs shot shot-pier" role="img" aria-label="Couple standing on a long pier at dusk over the water"></div>

  <section class="abs package package-photo">
    <svg class="icon" viewBox="0 0 26 24"><rect width="26" height="24" rx="3" fill="var(--salmon)"/><rect x="5" y="7" width="16" height="11" rx="2" fill="none" stroke="#fff" stroke-width="1.6"/><circle cx="13" cy="12.5" r="3" fill="none" stroke="#fff" stroke-width="1.6"/><rect x="9" y="5" width="5" height="2" fill="#fff"/></svg>
    <h2>Photo Package Includes</h2>
    <ul>
      <li><svg viewBox="0 0 10 10"><circle cx="5" cy="5" r="4.4" fill="none" stroke="#666"/><path d="M2.8 5.2l1.6 1.6 3-3.4" fill="none" stroke="#666" stroke-width="1.2"/></svg>1 Hr Engagement Shoot</li>
      <li><svg viewBox="0 0 10 10"><circle cx="5" cy="5" r="4.4" fill="none" stroke="#666"/><path d="M2.8 5.2l1.6 1.6 3-3.4" fill="none" stroke="#666" stroke-width="1.2"/></svg>One photographer up to 7 hours on location for wedding</li>
      <li><svg viewBox="0 0 10 10"><circle cx="5" cy="5" r="4.4" fill="none" stroke="#666"/><path d="M2.8 5.2l1.6 1.6 3-3.4" fill="none" stroke="#666" stroke-width="1.2"/></svg>High Resolution, Edited digital images</li>
      <li><svg viewBox="0 0 10 10"><circle cx="5" cy="5" r="4.4" fill="none" stroke="#666"/><path d="M2.8 5.2l1.6 1.6 3-3.4" fill="none" stroke="#666" stroke-width="1.2"/></svg>Images professionally edited in house</li>
      <li><svg viewBox="0 0 10 10"><circle cx="5" cy="5" r="4.4" fill="none" stroke="#666"/><path d="M2.8 5.2l1.6 1.6 3-3.4" fill="none" stroke="#666" stroke-width="1.2"/></svg>Beautiful online gallery to download from</li>
      <li><svg viewBox="0 0 10 10"><circle cx="5" cy="5" r="4.4" fill="none" stroke="#666"/><path d="M2.8 5.2l1.6 1.6 3-3.4" fill="none" stroke="#666" stroke-width="1.2"/></svg>Print release to print at the lab of your choice</li>
      <li><svg viewBox="0 0 10 10"><circle cx="5" cy="5" r="4.4" fill="none" stroke="#666"/><path d="M2.8 5.2l1.6 1.6 3-3.4" fill="none" stroke="#666" stroke-width="1.2"/></svg>Normal Retail Price $2450</li>
    </ul>
  </section>

  <section class="abs package package-video">
    <svg class="icon" viewBox="0 0 26 24"><rect width="26" height="24" rx="3" fill="var(--periwinkle)"/><rect x="4" y="8" width="12" height="9" rx="1.5" fill="#fff"/><path d="M16 12.5l6-3.5v7z" fill="#fff"/></svg>
    <h2>Video Package Includes</h2>
    <ul>
      <li><svg viewBox="0 0 10 10"><circle cx="5" cy="5" r="4.4" fill="none" stroke="#666"/><path d="M2.8 5.2l1.6 1.6 3-3.4" fill="none" stroke="#666" stroke-width="1.2"/></svg>Up To 6 Hours of Coverage</li>
      <li><svg viewBox="0 0 10 10"><circle cx="5" cy="5" r="4.4" fill="none" stroke="#666"/><path d="M2.8 5.2l1.6 1.6 3-3.4" fill="none" stroke="#666" stroke-width="1.2"/></svg>Documentary Style Video Edit 60-90 Minutes</li>
      <li><svg viewBox="0 0 10 10"><circle cx="5" cy="5" r="4.4" fill="none" stroke="#666"/><path d="M2.8 5.2l1.6 1.6 3-3.4" fill="none" stroke="#666" stroke-width="1.2"/></svg>Edited Background Music</li>
      <li><svg viewBox="0 0 10 10"><circle cx="5" cy="5" r="4.4" fill="none" stroke="#666"/><path d="M2.8 5.2l1.6 1.6 3-3.4" fill="none" stroke="#666" stroke-width="1.2"/></svg>A Cinematic highlight Recap 3-4 minutes</li>
      <li><svg viewBox="0 0 10 10"><circle cx="5" cy="5" r="4.4" fill="none" stroke="#666"/><path d="M2.8 5.2l1.6 1.6 3-3.4" fill="none" stroke="#666" stroke-width="1.2"/></svg>3 Personalized DVDs</li>
      <li><svg viewBox="0 0 10 10"><circle cx="5" cy="5" r="4.4" fill="none" stroke="#666"/><path d="M2.8 5.2l1.6 1.6 3-3.4" fill="none" stroke="#666" stroke-width="1.2"/></svg>Normal retail Price $1299</li>
    </ul>
  </section>

  <svg class="abs badge" viewBox="0 0 100 100" aria-label="Plus save 10% off any upgrades">
    <polygon fill="var(--badge)" points="50,2 56,9 64,4 68,12 77,10 78,19 87,20 86,29 94,33 90,41 97,47 91,54 96,62 88,66 90,75 81,77 80,86 71,85 67,93 59,89 53,96 47,90 39,95 35,87 26,89 24,80 15,79 17,70 8,66 13,58 5,52 11,45 5,38 13,33 11,24 20,22 20,13 29,14 32,5 41,9 45,1"/>
    <circle cx="50" cy="50" r="37" fill="none" stroke="#fff" stroke-width="1" stroke-dasharray="2 2"/>
    <text x="50" y="38" text-anchor="middle" fill="#fff" font-family="Open Sans, Arial, sans-serif" font-size="10">Plus Save</text>
    <text x="47" y="60" text-anchor="middle" fill="#fff" font-family="Roboto Slab, Georgia, serif" font-weight="700" font-size="20">10%</text>
    <text x="71" y="51" fill="#fff" font-family="Open Sans, Arial, sans-serif" font-size="7">off</text>
    <text x="50" y="71" text-anchor="middle" fill="#fff" font-family="Open Sans, Arial, sans-serif" font-size="7">any upgrades</text>
  </svg>

  <div class="abs band band-photo"><span class="label">Photo Contact Info</span><b>555-210-4837</b><span class="sep">|</span><b>brightoakportraitstudio.com</b></div>
  <div class="abs band band-video"><span class="label">Video Contact info</span><b>555-318-2264</b><span class="sep">|</span><b>www.qmtrz.com</b></div>
</main>
</body>
</html>
```